Spice Mix Label Bottle Branding - Health and Weight Loss Mixes

The company is called ZestRow Spice Mix's. We've created 5 spice mixes using ingredients that promote health and weight loss. We already have a logo but now we need labels for our bottles. We would like to see designs that have the feel of health supplements (see attached examples)

We would like a different colour featured with each of our flavours.

Our flavours are:
-Golden Chai (Yellow)
-Mild Curry (Orange)
-Coffee Rub (brown)
-Garlic Oregano (Green)
-Taco (Blue)

Thank you!

Target Market(s)

Ages 22-35. Men and Female. Trendy, Hipster.

Industry/Entity Type

Food Production

Font styles to use
Sans Serif

Colors
f37122
0655a3
0692cd
9bcb3c
fbee3f

Requirements
Must have
• A different featured colour for each flavour.
• The ZestRow Spices Logo (attached)
• The slogan: "Weight Loss Ingredients"
• -Golden Chai (Yellow)
• -Mild Curry (Orange)
• -Coffee Rub (brown)
• -Garlic Oregano (Green)
• -Taco (Blue)
• Text Files attached.
Nice to have
• A black label with a featured colour for each of the spice mice flavours.
• 'No Salt added'

```html
<!DOCTYPE html>
<html lang="en">
<head>
<meta charset="utf-8">
<title>ZestRow Spices – Label Range</title>
<link href="https://fonts.googleapis.com/css2?family=Montserrat:wght@600;800&family=Oswald:wght@500;600&display=swap" rel="stylesheet">
<style>
  :root {
    --bg: #ffffff;
    --label-black: #121212;
    --label-black-soft: #242424;
    --white: #ffffff;
    --chai: #d9a521;
    --curry: #f05a1a;
    --oregano: #9bbd3a;
    --coffee: #8e5c2e;
    --taco: #2f6aa8;
  }
  * { box-sizing: border-box; margin: 0; padding: 0; }
  html, body {
    width: 1200px; height: 483px; overflow: hidden;
    background: var(--bg);
  }
  .label-range {
    width: 1200px; height: 483px;
    display: flex; align-items: center; justify-content: space-between;
    padding: 0 62px;
  }
  .label {
    --accent: var(--chai);
    width: 168px; height: 186px;
    background: var(--accent);
    padding: 6px;
  }
  .label--chai { --accent: var(--chai); }
  .label--curry { --accent: var(--curry); }
  .label--oregano { --accent: var(--oregano); }
  .label--coffee { --accent: var(--coffee); }
  .label--taco { --accent: var(--taco); }

  .label__panel {
    width: 100%; height: 100%;
    background: radial-gradient(ellipse at 70% 20%, var(--label-black-soft) 0%, var(--label-black) 60%);
    display: flex; flex-direction: column; align-items: center;
    padding-top: 14px;
  }
  .brand {
    display: flex; align-items: center; gap: 5px;
    font-family: "Montserrat", sans-serif; font-weight: 800;
    font-size: 15px; color: var(--white); letter-spacing: 0.2px;
  }
  .brand__mark {
    width: 8px; height: 8px; background: var(--accent);
  }
  .brand__tagline {
    margin-top: 4px;
    font-family: "Montserrat", sans-serif; font-weight: 600;
    font-size: 5px; letter-spacing: 0.4px; color: var(--white);
  }
  .flavour {
    margin-top: 18px;
    width: 96px; height: 38px;
    border: 2px solid var(--accent);
    padding: 2px;
  }
  .flavour__inner {
    width: 100%; height: 100%;
    border: 1px solid var(--accent);
    display: flex; align-items: center; justify-content: center;
    text-align: center;
    font-family: "Montserrat", sans-serif; font-weight: 800;
    font-size: 9.5px; line-height: 1.15; letter-spacing: 2.2px;
    color: var(--white); text-transform: uppercase;
  }
  .flavour__inner--single { font-size: 15px; letter-spacing: 3px; }
  .slogan {
    margin-top: 16px;
    font-family: "Oswald", sans-serif; font-weight: 600;
    font-size: 8px; color: var(--accent);
  }
  .divider { margin-top: 1px; width: 84px; height: 4px; display: block; }
  .no-salt {
    margin-top: 1px;
    font-family: "Montserrat", sans-serif; font-weight: 800;
    font-size: 4.5px; letter-spacing: 0.4px; color: var(--white);
  }
</style>
</head>
<body>
<main class="label-range">

  <article class="label label--chai">
    <div class="label__panel">
      <div class="brand"><span class="brand__mark"></span>ZestRow Spices</div>
      <div class="brand__tagline">WEIGHT LOSS SEASONINGS</div>
      <div class="flavour"><div class="flavour__inner">Golden<br>Chai</div></div>
      <div class="slogan">Weight Loss Ingredients</div>
      <svg class="divider" viewBox="0 0 84 4"><line x1="0" y1="2" x2="84" y2="2" stroke="var(--accent)" stroke-width="0.6"/><circle cx="2" cy="2" r="1.2" fill="var(--accent)"/><circle cx="82" cy="2" r="1.2" fill="var(--accent)"/></svg>
      <div class="no-salt">NO SALT ADDED</div>
    </div>
  </article>

  <article class="label label--curry">
    <div class="label__panel">
      <div class="brand"><span class="brand__mark"></span>ZestRow Spices</div>
      <div class="brand__tagline">WEIGHT LOSS SEASONINGS</div>
      <div class="flavour"><div class="flavour__inner">Mild<br>Curry</div></div>
      <div class="slogan">Weight Loss Ingredients</div>
      <svg class="divider" viewBox="0 0 84 4"><line x1="0" y1="2" x2="84" y2="2" stroke="var(--accent)" stroke-width="0.6"/><circle cx="2" cy="2" r="1.2" fill="var(--accent)"/><circle cx="82" cy="2" r="1.2" fill="var(--accent)"/></svg>
      <div class="no-salt">NO SALT ADDED</div>
    </div>
  </article>

  <article class="label label--oregano">
    <div class="label__panel">
      <div class="brand"><span class="brand__mark"></span>ZestRow Spices</div>
      <div class="brand__tagline">WEIGHT LOSS SEASONINGS</div>
      <div class="flavour"><div class="flavour__inner">Garlic<br>Oregano</div></div>
      <div class="slogan">Weight Loss Ingredients</div>
      <svg class="divider" viewBox="0 0 84 4"><line x1="0" y1="2" x2="84" y2="2" stroke="var(--accent)" stroke-width="0.6"/><circle cx="2" cy="2" r="1.2" fill="var(--accent)"/><circle cx="82" cy="2" r="1.2" fill="var(--accent)"/></svg>
      <div class="no-salt">NO SALT ADDED</div>
    </div>
  </article>

  <article class="label label--coffee">
    <div class="label__panel">
      <div class="brand"><span class="brand__mark"></span>ZestRow Spices</div>
      <div class="brand__tagline">WEIGHT LOSS SEASONINGS</div>
      <div class="flavour"><div class="flavour__inner">Coffee<br>Rub</div></div>
      <div class="slogan">Weight Loss Ingredients</div>
      <svg class="divider" viewBox="0 0 84 4"><line x1="0" y1="2" x2="84" y2="2" stroke="var(--accent)" stroke-width="0.6"/><circle cx="2" cy="2" r="1.2" fill="var(--accent)"/><circle cx="82" cy="2" r="1.2" fill="var(--accent)"/></svg>
      <div class="no-salt">NO SALT ADDED</div>
    </div>
  </article>

  <article class="label label--taco">
    <div class="label__panel">
      <div class="brand"><span class="brand__mark"></span>ZestRow Spices</div>
      <div class="brand__tagline">WEIGHT LOSS SEASONINGS</div>
      <div class="flavour"><div class="flavour__inner flavour__inner--single">Taco</div></div>
      <div class="slogan">Weight Loss Ingredients</div>
      <svg class="divider" viewBox="0 0 84 4"><line x1="0" y1="2" x2="84" y2="2" stroke="var(--accent)" stroke-width="0.6"/><circle cx="2" cy="2" r="1.2" fill="var(--accent)"/><circle cx="82" cy="2" r="1.2" fill="var(--accent)"/></svg>
      <div class="no-salt">NO SALT ADDED</div>
    </div>
  </article>

</main>
</body>
</html>
```